Business card for a boutique travel agency VELARIEN

we need a business card design - double sided. We would like to have a very elegant, sophisticated but modern design. we are travel consultants and our business focus is Europe, mainly the city of Paris. We would like to receive designs in white and silver, black color but if you are confident that we should pick up a color to make it different and more beautful...go ahead! We are going to give business cards to our clients and business partners. It is important to be perceived as elegant, modern and trustful. Please check jpg references.

Target Market(s)

Velarien primary clients are individuals, couples and affinity groups of high-net-worth who travel for leisure at least once per year. Seeking the ultimate travel experience, the target clients demand the finest quality activities and accommodations accompanied by a superior level of service.

Industry/Entity Type

Travel Industry

Contact Information for Business Card

Lucinda Farrow
- lucinda@velarien-example.com
- +55 11 98347.2516
- velarien-example.com
- unique travel experiences (we would like to see this signature printed as a detail)

Font styles to use
Sans Serif

Colors

Designer to choose colors to be used in the design.

Requirements
Must have
• the Velarien logo that I have attached
Nice to have
• we would like to have some nice detail, something different that shows that we care about,... we are detail oriented.
Should not have
• decorative fonts

```html
<!DOCTYPE html>
<html lang="en">
<head>
<meta charset="utf-8">
<title>Velarien — Business Card</title>
<link rel="stylesheet" href="https://fonts.googleapis.com/css2?family=Open+Sans:wght@400&display=swap">
<style>
  :root {
    --backdrop: #3b4048;
    --card: #1f1f20;
    --card-edge: #141414;
    --ink: #f2f2f2;
    --accent: #3d9ee0;
  }
  * { margin: 0; padding: 0; box-sizing: border-box; }
  html, body {
    width: 1200px; height: 900px; overflow: hidden;
    background: var(--backdrop);
    font-family: "Open Sans", Arial, sans-serif;
  }
  .stage {
    width: 1200px; height: 900px;
    display: flex; flex-direction: column;
    align-items: center; justify-content: center; gap: 60px;
  }
  .card {
    position: relative;
    width: 620px; height: 354px;
    background: var(--card);
    border: 1px solid var(--card-edge);
    box-shadow: 0 10px 24px rgba(0,0,0,.35);
    color: var(--ink);
  }
  .wordmark {
    font-weight: 400; font-size: 26px;
    letter-spacing: 0.08em; color: var(--ink);
    white-space: nowrap;
  }
  .card-front .wordmark { position: absolute; top: 46px; left: 46px; }
  .holder-name {
    position: absolute; top: 140px; left: 46px;
    font-size: 17px; font-weight: 400; letter-spacing: 0.02em;
    text-transform: uppercase;
  }
  .contact-list {
    position: absolute; right: 46px; bottom: 40px;
    list-style: none; display: flex; flex-direction: column; gap: 6px;
    font-size: 16px; font-weight: 400;
  }
  .contact-item { display: flex; align-items: center; gap: 10px; }
  .contact-icon { width: 14px; height: 14px; flex: none; fill: var(--accent); }
  .card-back { display: flex; align-items: center; justify-content: center; }
  .card-back .wordmark { font-size: 30px; margin-top: 30px; }
</style>
</head>
<body>
<main class="stage">
  <section class="card card-front" aria-label="Card front">
    <div class="wordmark">VELARIEN</div>
    <p class="holder-name">Lucinda Farrow</p>
    <ul class="contact-list">
      <li class="contact-item">
        <svg class="contact-icon" viewBox="0 0 16 16" aria-hidden="true"><path d="M3.5 1.5l2.5 0 1 3.5-1.7 1.2a8 8 0 0 0 4.5 4.5L11 9l3.5 1v2.5c0 1-1 2-2 2C6.5 14.5 1.5 9.5 1.5 3.5c0-1 1-2 2-2z"/></svg>
        <span>+55 11 98347.2516</span>
      </li>
      <li class="contact-item">
        <svg class="contact-icon" viewBox="0 0 16 16" aria-hidden="true"><path d="M1 3h14v10H1z M1.5 3.5L8 9l6.5-5.5" stroke="#1f1f20" stroke-width="1.2"/></svg>
        <span>lucinda@velarien-example.com</span>
      </li>
      <li class="contact-item">
        <svg class="contact-icon" viewBox="0 0 16 16" aria-hidden="true"><circle cx="8" cy="8" r="7"/><path d="M1 8h14M8 1c-3 3.5-3 10.5 0 14M8 1c3 3.5 3 10.5 0 14" fill="none" stroke="#1f1f20" stroke-width="1"/></svg>
        <span>www.velarien-example.com</span>
      </li>
    </ul>
  </section>

  <section class="card card-back" aria-label="Card back">
    <div class="wordmark">VELARIEN</div>
  </section>
</main>
</body>
</html>
```